Fence & Deck Construction Flyer

My company is called Brackley Fence & Deck and I am seeking a flyer for direct marketing our construction services to residential customers in Calgary. Our focus is home owners aged 35+ that are looking to replace an old fence or deck, although we also do new construction. We use pressure treated wood mainly, but we also use cedar and composite products. You can view our website at www.brackleyfence.ca for some additional insight and pictures of our previous projects. Company colors are black and deep yellow (see website).
The size of the flyer will need to be 6 inches by 11 inches, both sides in full colour.

```html
<!DOCTYPE html>
<html lang="en">
<head>
<meta charset="utf-8">
<title>Brackley Fence &amp; Deck — Flyer</title>
<link href="https://fonts.googleapis.com/css2?family=Poppins:wght@200;500;600;700&display=swap" rel="stylesheet">
<style>
  :root {
    --black: #0b0b0b;
    --yellow: #ffd400;
    --white: #ffffff;
    --stage: #e9e9e9;
    --label: #9a9a9a;
    --wood-light: #c29a70;
    --wood-mid: #9a6a3e;
    --wood-dark: #6e4322;
    --pool: #2f5fb8;
    --contact-band: rgba(24, 18, 12, 0.86);
  }
  * { box-sizing: border-box; margin: 0; padding: 0; }
  html, body { width: 1200px; height: 900px; overflow: hidden; }
  body {
    position: relative;
    background: var(--stage);
    font-family: "Poppins", "Century Gothic", sans-serif;
    color: var(--white);
  }
  .side-label {
    position: absolute;
    font-weight: 200;
    font-size: 40px;
    color: var(--label);
  }
  .side-label--front { left: 874px; top: 190px; }
  .side-label--back { left: 272px; top: 650px; }

  .flyer {
    position: absolute;
    width: 792px;
    height: 432px;
    overflow: hidden;
  }

  /* Front side */
  .flyer--front { left: 56px; top: 35px; }
  .front-photo {
    position: absolute; inset: 0;
    background: linear-gradient(100deg, var(--pool) 0%, var(--wood-mid) 45%, var(--wood-light) 100%);
  }
  .front-panel {
    position: absolute;
    left: 36px; top: 151px;
    width: 291px; height: 281px;
    background: var(--black);
    border-radius: 16px 16px 0 0;
  }
  .brand {
    display: flex; align-items: center; gap: 10px;
    color: var(--yellow);
    font-weight: 600;
    line-height: 1.05;
  }
  .brand__mark { background: var(--yellow); flex: none; }
  .front-panel .brand { position: absolute; left: 22px; top: 34px; font-size: 27px; }
  .front-panel .brand__mark { width: 44px; height: 44px; }
  .tagline { font-weight: 500; color: var(--white); white-space: nowrap; }
  .front-panel .tagline {
    position: absolute; left: 20px; top: 113px; font-size: 10.5px;
  }
  .front-phone {
    position: absolute; left: 0; top: 159px; width: 100%; height: 22px;
    background: var(--yellow); color: var(--black);
    text-align: center; font-size: 15px; font-weight: 500; line-height: 22px;
  }
  .front-address {
    position: absolute; left: 26px; top: 187px;
    font-size: 7.5px; color: var(--yellow); font-weight: 500;
    white-space: nowrap;
  }
  .front-address span + span { margin-left: 12px; }
  .front-web {
    position: absolute; left: 26px; top: 245px;
    font-size: 8.5px; font-weight: 500; white-space: nowrap;
  }

  /* Back side */
  .flyer--back { left: 389px; top: 440px; }
  .back-rail-photo {
    position: absolute; left: 0; top: 0; width: 100%; height: 80px;
    background: linear-gradient(180deg, #b8916a 0%, var(--wood-dark) 100%);
  }
  .back-body {
    position: absolute; left: 0; top: 80px; width: 100%; height: 213px;
    background: var(--black);
  }
  .back-body .brand { position: absolute; left: 46px; top: 50px; font-size: 38px; }
  .back-body .brand__mark { width: 62px; height: 62px; }
  .back-body .tagline { position: absolute; left: 44px; top: 156px; font-size: 14px; }
  .back-divider {
    position: absolute; left: 432px; top: 22px; width: 2px; height: 166px;
    background: var(--yellow);
  }
  .back-about {
    position: absolute; left: 466px; top: 44px; width: 300px;
    font-size: 11.2px; font-weight: 500; line-height: 1.45;
  }
  .back-online {
    position: absolute; left: 466px; top: 155px;
    font-size: 12.5px; font-weight: 700; white-space: nowrap;
  }
  .back-online a { color: var(--yellow); text-decoration: none; }
  .back-callout {
    position: absolute; left: 0; top: 293px; width: 100%; height: 32px;
    background: var(--yellow); color: var(--black);
    display: flex; align-items: center; justify-content: space-between;
    padding: 0 32px 0 42px;
  }
  .back-callout__text { font-size: 12px; font-weight: 700; white-space: nowrap; }
  .back-callout__phone { font-size: 19px; font-weight: 500; white-space: nowrap; }
  .back-deck-photo {
    position: absolute; left: 0; top: 325px; width: 100%; height: 107px;
    background: linear-gradient(180deg, var(--wood-mid) 0%, var(--wood-light) 100%);
  }
  .back-contact {
    position: absolute; left: 0; top: 325px; width: 100%; height: 43px;
    background: var(--contact-band);
    display: flex; align-items: center; justify-content: space-between;
    padding: 0 32px 0 43px;
    font-size: 9px; font-weight: 500; color: var(--yellow); white-space: nowrap;
  }
</style>
</head>
<body>
  <span class="side-label side-label--front">Front</span>
  <span class="side-label side-label--back">Back</span>

  <section class="flyer flyer--front">
    <div class="front-photo" role="img" aria-label="Photo of a wooden deck with vertical-slat railing around an above-ground pool, lawn and tree behind"></div>
    <div class="front-panel">
      <div class="brand"><span class="brand__mark"></span><span>Brackley<br>Fence &amp; Deck</span></div>
      <p class="tagline">The residential wood deck and fence specialists.</p>
      <div class="front-phone">(403) 555-0148</div>
      <p class="front-address"><span>42 Harwick Ridge Place NW</span><span>Calgary, AB Canada T3A 0K2</span></p>
      <p class="front-web">www.brackleyfence.ca &nbsp;/&nbsp; brackleyfencedeck@mail.com</p>
    </div>
  </section>

  <section class="flyer flyer--back">
    <div class="back-rail-photo" role="img" aria-label="Photo of wooden deck railing balusters against a white background"></div>
    <div class="back-body">
      <div class="brand"><span class="brand__mark"></span><span>Brackley<br>Fence &amp; Deck</span></div>
      <p class="tagline">The residential wood deck and fence specialists.</p>
      <div class="back-divider"></div>
      <p class="back-about">We are the trusted and referred leader in residential wood fence and deck sales and installation. If you are looking for a reputable full service builder, we have the expertise you need and the service you can trust, at a price you can afford.</p>
      <p class="back-online">Find us online @ <a href="http://www.brackleyfence.ca">http://www.brackleyfence.ca</a></p>
    </div>
    <div class="back-callout">
      <span class="back-callout__text">Call us today for a free professional on-site consulation and quote for your project.</span>
      <span class="back-callout__phone">(403) 555-0148</span>
    </div>
    <div class="back-deck-photo" role="img" aria-label="Photo of wet wooden deck boards with water droplets"></div>
    <div class="back-contact">
      <span>42 Harwick Ridge Place NW &nbsp;/&nbsp; Calgary, Alberta &nbsp;&nbsp; T3A 0K2</span>
      <span>brackleyfencedeck@mail.com</span>
    </div>
  </section>
</body>
</html>
```